GILDED BRICKWORK: THE DEPENDABLE ROUTE WHEREBY MODEST HOUSING FLIPS YIELD HANDSOME RETURNS

I am looking for a book cover design for my new E-Book.

My idea for the design is a pin board with before and after photos of our properties pinned on it (example attached). I have also attached some photos to use.

PLEASE SUBMIT OTHER DESIGNS ALSO AS THIS WAS JUST AN IDEA BUT I AM OPEN TO OTHER IDEAS ALSO.

Page size is 5x7 inches

Font styles to use
Serif
Sans Serif

Colors
0255a3
3176b5
85acd3
85cae6
33a6d7
0392cd
9bcb3c
abd036
ec1f27

```html
<!DOCTYPE html>
<html lang="en">
<head>
<meta charset="utf-8">
<title>Gilded Brickwork – E-Book Cover</title>
<link rel="stylesheet" href="https://fonts.googleapis.com/css2?family=Oswald:wght@400;500;600;700&display=swap">
<style>
  :root {
    --page-bg: #eeeeee;
    --cover-bg: #ffffff;
    --title-red: #c81c3a;
    --subtitle-green: #17963f;
    --band-blue: #17488b;
    --band-text: #ffffff;
    --site-wood-light: #d9b488;
    --site-wood-dark: #a8743f;
    --site-ground: #c9b79a;
    --house-sky: #eef0f2;
    --house-siding: #8a8c90;
    --house-lawn: #5a9a2c;
  }
  html, body {
    margin: 0;
    padding: 0;
    width: 1200px;
    height: 1186px;
    overflow: hidden;
    background: var(--page-bg);
  }
  .cover {
    position: absolute;
    left: 154px;
    top: 0;
    width: 892px;
    height: 1186px;
    background: var(--cover-bg);
    font-family: "Oswald", sans-serif;
    overflow: hidden;
  }
  .cover-title {
    margin: 0;
    position: absolute;
    left: 0;
    width: 100%;
    top: 30px;
    text-align: center;
    color: var(--title-red);
    text-transform: uppercase;
    line-height: 1;
  }
  .cover-title__lead {
    display: block;
    font-weight: 500;
    font-size: 142px;
    letter-spacing: 2px;
    white-space: nowrap;
  }
  .cover-title__main {
    display: block;
    font-weight: 700;
    font-size: 165px;
    letter-spacing: 1px;
    margin-top: 8px;
    white-space: nowrap;
  }
  .cover-subtitle {
    position: absolute;
    left: 0;
    width: 100%;
    top: 398px;
    margin: 0;
    text-align: center;
    color: var(--subtitle-green);
    font-weight: 400;
    font-size: 56px;
    line-height: 62px;
    text-transform: uppercase;
  }
  .cover-photos {
    position: absolute;
    left: 0;
    top: 620px;
    width: 100%;
    height: 404px;
    display: flex;
  }
  .photo-before {
    width: 46%;
    height: 100%;
    background:
      linear-gradient(180deg, var(--house-sky) 0%, var(--house-sky) 8%, transparent 8%),
      linear-gradient(180deg, var(--site-wood-light) 0%, var(--site-wood-dark) 78%, var(--site-ground) 78%, var(--site-ground) 100%);
  }
  .photo-after {
    width: 54%;
    height: 100%;
    background: linear-gradient(180deg, var(--house-sky) 0%, var(--house-siding) 20%, var(--house-siding) 74%, var(--house-lawn) 74%, var(--house-lawn) 100%);
  }
  .author-band {
    position: absolute;
    left: 0;
    top: 1024px;
    width: 100%;
    height: 162px;
    background: var(--band-blue);
    display: flex;
    align-items: center;
    justify-content: center;
  }
  .author-name {
    color: var(--band-text);
    font-weight: 500;
    font-size: 92px;
    line-height: 1;
  }
</style>
</head>
<body>
  <main class="cover">
    <h1 class="cover-title">
      <span class="cover-title__lead">Gilded</span>
      <span class="cover-title__main">Brickwork</span>
    </h1>
    <p class="cover-subtitle">The dependable route whereby<br>modest housing flips yield<br>handsome returns</p>
    <div class="cover-photos">
      <div class="photo-before" role="img" aria-label="Before photo: house under construction with bare plywood walls and scaffolding"></div>
      <div class="photo-after" role="img" aria-label="After photo: finished grey-sided house with white porch railing and green lawn"></div>
    </div>
    <div class="author-band">
      <span class="author-name">Marcus Ellery</span>
    </div>
  </main>
</body>
</html>
```